MOLVT Study flyer

I need help designing a flyer for a research study that will include brain imaging in adolescents. The info is in the attached document. The study is called the Marrowby Orchard Lantern Vesper Trail (MOLVT) study. Ideally this would be returned as a document that I can edit in the future as we will have several new recruitment phases (different age groups, etc. I also would love to have a logo designed as part of this project, but I recognize that might be a separate design request.

```html
<!DOCTYPE html>
<html lang="en">
<head>
<meta charset="utf-8">
<title>MOLVT Study Flyer</title>
<link rel="stylesheet" href="https://fonts.googleapis.com/css2?family=Poppins:wght@400;500;600;700;800&display=swap">
<style>
  :root {
    --navy: #0b1f6e;
    --blue: #0a3fc4;
    --yellow: #fbbd18;
    --ink: #3b3b3b;
    --muted: #a2a2a2;
    --line: #555555;
    --paper: #ffffff;
  }
  * { margin: 0; padding: 0; box-sizing: border-box; }
  html, body { width: 902px; height: 1200px; overflow: hidden; background: var(--paper); }
  body { font-family: "Poppins", sans-serif; color: var(--ink); }
  .flyer { position: relative; width: 902px; height: 1200px; background: var(--paper); }

  .study-name { position: absolute; left: 80px; top: 60px; font-weight: 800; font-size: 21px; line-height: 27px; color: var(--navy); }
  .study-name .accent { color: var(--blue); }
  .study-title { position: absolute; left: 78px; top: 138px; font-weight: 800; font-size: 51px; line-height: 60px; color: var(--navy); letter-spacing: -0.5px; }

  .brain-visual { position: absolute; left: 443px; top: 100px; width: 406px; height: 370px;
    border-radius: 48% 52% 40% 45% / 50% 50% 45% 50%;
    background: radial-gradient(ellipse at 45% 40%, #f2b89c 0%, #e39a7c 55%, #c9725a 100%); }

  .question-band { position: absolute; left: 72px; top: 208px; width: 400px; height: 152px; }
  .question { position: absolute; left: 109px; display: flex; align-items: center; gap: 9px; color: #fff; font-size: 16px; line-height: 19px; }
  .question .q-mark { width: 33px; height: 33px; border-radius: 6px; background: var(--yellow); color: #fff; font-weight: 800; font-size: 26px; display: flex; align-items: center; justify-content: center; flex: none; }
  .question strong { font-weight: 700; }
  .q1 { top: 240px; }
  .q2 { top: 293px; }

  .intro { position: absolute; left: 85px; top: 390px; width: 360px; font-size: 14.6px; line-height: 18px; color: var(--ink); }

  .section-heading { position: absolute; left: 80px; top: 492px; font-weight: 800; font-size: 29.5px; color: var(--navy); letter-spacing: -0.3px; }
  .section-heading .accent, .eligibility-heading .accent { color: var(--blue); }

  .step { position: absolute; left: 82px; width: 739px; height: 94px; border: 1.2px solid var(--line); display: flex; align-items: center; }
  .step .step-icon { width: 50px; height: 50px; margin-left: 20px; flex: none; }
  .step p { margin-left: 18px; max-width: 620px; font-weight: 600; font-size: 15.6px; line-height: 19.5px; color: var(--ink); }
  .step .note { color: var(--muted); }
  .step-1 { top: 552px; }
  .step-2 { top: 659px; }
  .step-3 { top: 765px; }

  .kids-visual { position: absolute; left: 80px; top: 892px; width: 318px; height: 186px; border-radius: 10px;
    background: linear-gradient(160deg, #f3c9a8 0%, #e0524a 35%, #f1c232 55%, #3a6fc9 80%, #9aa4b1 100%); opacity: 0.85; }

  .eligibility-heading { position: absolute; left: 410px; top: 889px; font-weight: 800; font-size: 24.5px; color: var(--navy); letter-spacing: -0.3px; }
  .criteria { position: absolute; left: 424px; top: 936px; list-style: none; width: 400px; }
  .criteria li { position: relative; padding-left: 15px; font-size: 16px; line-height: 19.5px; margin-bottom: 7.5px; color: var(--ink); }
  .criteria li svg { position: absolute; left: -1px; top: 3px; width: 15px; height: 15px; }
  .criteria li span { display: block; margin-left: 1px; }
  .criteria strong { font-weight: 700; }

  .compensation { position: absolute; left: 417px; top: 1050px; width: 408px; height: 42px; }
  .compensation span { position: absolute; left: 0; top: 0; width: 100%; height: 38px; display: flex; align-items: center; justify-content: center; font-weight: 700; font-size: 18.5px; letter-spacing: 4.4px; color: var(--navy); }

  .contact-bar { position: absolute; left: 80px; top: 1108px; width: 742px; height: 35px; background: var(--navy); display: flex; align-items: center; font-weight: 700; font-size: 13.6px; color: #fff; overflow: hidden; }
  .contact-bar .lead { color: var(--yellow); margin-left: 13px; margin-right: 7px; white-space: nowrap; }
  .contact-bar .message { white-space: nowrap; }
  .contact-bar .email { margin-left: auto; width: 198px; height: 100%; background: var(--blue); display: flex; align-items: center; justify-content: center; white-space: nowrap; flex: none; }
</style>
</head>
<body>
<div class="flyer">

  <div class="study-name">
    <span class="accent">Marrowby</span><br>
    Orchard <span class="accent">Lantern</span><br>
    <span class="accent">Vesper</span> Trail
  </div>
  <h1 class="study-title">MOLVT study</h1>

  <div class="brain-visual" role="img" aria-label="Photograph of an anatomical model of a human brain"></div>

  <svg class="question-band" viewBox="0 0 400 152" preserveAspectRatio="none" aria-hidden="true">
    <path fill="#0b1f6e" d="M2 6 L20 3 L35 7 L52 2 L70 6 L90 3 L108 8 L125 4 L142 7 L160 2 L178 6 L198 3 L215 8 L232 4 L250 7 L268 2 L285 6 L303 3 L322 8 L340 4 L358 6 L376 3 L400 6 L400 146 L380 149 L362 145 L344 150 L326 146 L308 149 L290 145 L272 150 L254 146 L236 149 L218 145 L200 150 L182 146 L164 149 L146 145 L128 150 L110 146 L92 149 L74 145 L56 150 L38 146 L20 149 L4 146 L7 128 L3 108 L8 88 L4 66 L9 46 L4 26 Z"/>
  </svg>
  <div class="question q1"><span class="q-mark">?</span><span>Are you the parent of a child<br><strong>age 10-17?</strong></span></div>
  <div class="question q2"><span class="q-mark">?</span><span>Do they worry or overthink<br><strong>negative emotions?</strong></span></div>

  <p class="intro">Halvern State University researchers are seeking girls age 10-17 for a study about brain activity in emotions and decision-making and how they relate to puberty, anxiety and depression.</p>

  <h2 class="section-heading">Study participation <span class="accent">involves</span></h2>

  <div class="step step-1">
    <svg class="step-icon" viewBox="0 0 50 50" aria-hidden="true">
      <rect x="10" y="2" width="22" height="14" rx="7" fill="#fbbd18"/>
      <path d="M14 15 L12 20 L19 15 Z" fill="#fbbd18"/>
      <circle cx="16" cy="9" r="1.6" fill="#fff"/><circle cx="21" cy="9" r="1.6" fill="#fff"/><circle cx="26" cy="9" r="1.6" fill="#fff"/>
      <circle cx="25" cy="24" r="4" fill="#fbbd18"/>
      <circle cx="12" cy="29" r="3.5" fill="#fbbd18"/><circle cx="38" cy="29" r="3.5" fill="#fbbd18"/>
      <path d="M18 42 Q18 30 25 30 Q32 30 32 42 Z" fill="#fbbd18"/>
      <path d="M5 46 Q5 34 12 34 Q18 34 18 46 Z" fill="#fbbd18"/>
      <path d="M32 46 Q32 34 38 34 Q45 34 45 46 Z" fill="#fbbd18"/>
      <rect x="2" y="42" width="46" height="4" fill="#fbbd18"/>
    </svg>
    <p>One one-hour interview <span class="note">(online or in-person)</span> where your child will discuss their thoughts</p>
  </div>

  <div class="step step-2">
    <svg class="step-icon" viewBox="0 0 50 50" aria-hidden="true">
      <rect x="6" y="14" width="34" height="24" rx="2" fill="none" stroke="#0a3fc4" stroke-width="3"/>
      <rect x="2" y="40" width="44" height="4" rx="1.5" fill="#0a3fc4"/>
      <circle cx="17" cy="24" r="3.5" fill="#0a3fc4"/>
      <path d="M11 34 Q11 28 17 28 Q23 28 23 34 Z" fill="#0a3fc4"/>
      <rect x="28" y="2" width="20" height="14" rx="2" fill="#0a3fc4"/>
      <path d="M31 15 L30 21 L36 15 Z" fill="#0a3fc4"/>
      <circle cx="33" cy="9" r="1.5" fill="#fff"/><circle cx="38" cy="9" r="1.5" fill="#fff"/><circle cx="43" cy="9" r="1.5" fill="#fff"/>
    </svg>
    <p>Online questionnaires <span class="note">(parent and child)</span></p>
  </div>

  <div class="step step-3">
    <svg class="step-icon" viewBox="0 0 50 50" aria-hidden="true">
      <rect x="9" y="3" width="12" height="10" rx="1.5" fill="none" stroke="#0b1f6e" stroke-width="2"/>
      <path d="M11 6 H19 M11 9 H19" stroke="#0b1f6e" stroke-width="1.5"/>
      <circle cx="32" cy="8" r="5.5" fill="none" stroke="#0b1f6e" stroke-width="2"/>
      <circle cx="9" cy="20" r="3.5" fill="#0b1f6e"/><circle cx="41" cy="20" r="3.5" fill="#0b1f6e"/>
      <path d="M3 34 Q3 25 9 25 Q14 25 15 32 L15 34 Z" fill="#0b1f6e"/>
      <path d="M35 34 L35 32 Q36 25 41 25 Q47 25 47 34 Z" fill="#0b1f6e"/>
      <rect x="12" y="31" width="26" height="4" fill="#0b1f6e"/>
      <rect x="20" y="35" width="10" height="12" fill="#0b1f6e"/>
      <path d="M4 34 V47 M14 40 V47 M36 40 V47 M46 34 V47" stroke="#0b1f6e" stroke-width="2.5"/>
    </svg>
    <p>One two-hour visit where your child will complete an MRI scan, answer questions about their puberty stage, and have a small hair sample taken to study puberty hormones</p>
  </div>

  <div class="kids-visual" role="img" aria-label="Photograph of a group of six children sitting together on the floor"></div>

  <h2 class="eligibility-heading">Your child may be eligible <span class="accent">if they</span></h2>
  <ul class="criteria">
    <li><svg viewBox="0 0 16 16" aria-hidden="true"><circle cx="8" cy="8" r="8" fill="#fbbd18"/><path d="M4.5 8.2 L7 10.6 L11.6 5.6" fill="none" stroke="#fff" stroke-width="1.8" stroke-linecap="round" stroke-linejoin="round"/></svg><span>&nbsp;Are <strong>age 10-17</strong></span></li>
    <li><svg viewBox="0 0 16 16" aria-hidden="true"><circle cx="8" cy="8" r="8" fill="#fbbd18"/><path d="M4.5 8.2 L7 10.6 L11.6 5.6" fill="none" stroke="#fff" stroke-width="1.8" stroke-linecap="round" stroke-linejoin="round"/></svg><span>&nbsp;Tend to <strong>worry or overthink negative thoughts</strong></span></li>
    <li><svg viewBox="0 0 16 16" aria-hidden="true"><circle cx="8" cy="8" r="8" fill="#fbbd18"/><path d="M4.5 8.2 L7 10.6 L11.6 5.6" fill="none" stroke="#fff" stroke-width="1.8" stroke-linecap="round" stroke-linejoin="round"/></svg><span>&nbsp;Have not been <strong>diagnosed with psychosis,<br>&nbsp;learning problems, or autism</strong></span></li>
  </ul>

  <div class="compensation">
    <svg viewBox="0 0 408 42" width="408" height="42" preserveAspectRatio="none" aria-hidden="true">
      <path fill="#d9d9d9" d="M4 8 L404 8 L406 40 L380 41 L350 39 L320 41 L290 39 L260 41 L230 39 L200 41 L170 39 L140 41 L110 39 L80 41 L50 39 L20 41 L4 40 Z"/>
      <path fill="#fbbd18" d="M2 3 L22 1 L44 4 L66 1 L88 3 L110 1 L132 4 L154 1 L176 3 L198 1 L220 4 L242 1 L264 3 L286 1 L308 4 L330 1 L352 3 L374 1 L396 4 L406 2 L404 14 L407 26 L404 37 L384 35 L362 38 L340 35 L318 38 L296 35 L274 38 L252 35 L230 38 L208 35 L186 38 L164 35 L142 38 L120 35 L98 38 L76 35 L54 38 L32 35 L10 38 L3 36 L5 24 L1 12 Z"/>
    </svg>
    <span>COMPENSATION UP TO $140</span>
  </div>

  <div class="contact-bar">
    <span class="lead">Interested in participating?</span>
    <span class="message">Want more information?&nbsp; Please contact us!</span>
    <span class="email">molvt@halvern.edu</span>
  </div>

</div>
</body>
</html>
```